Car transport business

We need a new business card design. Attached is our old card sample. I would just like to adjust the logo colors (blue and red) to be brighter. I changed my name to the brighter red and the word dispatcher to a brighter blue as an example. But you can adjust those colors further. And then perhaps you can use the same colors for the card design but use your imagination.

As a suggestion so the card stands out I would like to add a clip art of car carrier truck. Attached are examples of that as well

```html
<!DOCTYPE html>
<html lang="en">
<head>
<meta charset="utf-8">
<title>Northline Haul – Business Card</title>
<link href="https://fonts.googleapis.com/css2?family=Montserrat:wght@500;600;700&display=swap" rel="stylesheet">
<style>
  :root {
    --brand-blue: #1f74bd;
    --brand-red: #ec1c24;
    --card-white: #ffffff;
    --ink-dark: #2b2b2b;
    --stage: #e9e6e1;
  }
  * { margin: 0; padding: 0; box-sizing: border-box; }
  html, body {
    width: 1200px; height: 900px; overflow: hidden;
    background: var(--stage);
    font-family: "Montserrat", Arial, sans-serif;
  }
  .sheet {
    position: relative; width: 1200px; height: 900px;
    display: flex; flex-direction: column; align-items: center; justify-content: center;
    gap: 32px;
  }
  .card {
    position: relative; width: 640px; height: 366px; overflow: hidden;
    box-shadow: 0 6px 18px rgba(0,0,0,0.18);
  }
  .card-back { background: var(--brand-blue); display: flex; align-items: center; justify-content: center; }
  .card-front { background: var(--card-white); }

  .brand { display: flex; align-items: center; gap: 12px; }
  .brand-dot { width: 30px; height: 30px; border-radius: 50%; flex: none; }
  .brand-text { display: flex; flex-direction: column; }
  .brand-name { font-weight: 700; letter-spacing: 1px; line-height: 1; white-space: nowrap; }
  .brand-tagline { font-weight: 500; letter-spacing: 2.4px; text-transform: uppercase; margin-top: 6px; white-space: nowrap; }

  .card-back .brand-dot { background: var(--brand-red); }
  .card-back .brand-name { color: var(--card-white); font-size: 38px; }
  .card-back .brand-tagline { color: var(--card-white); font-size: 11px; }

  .card-front .brand { position: absolute; top: 58px; right: 34px; }
  .card-front .brand-dot { background: var(--brand-red); width: 24px; height: 24px; }
  .card-front .brand-name { color: var(--brand-blue); font-size: 27px; }
  .card-front .brand-tagline { color: var(--brand-blue); font-size: 8.5px; letter-spacing: 1.8px; }

  .holder { position: absolute; top: 46px; left: 44px; }
  .holder-name { font-size: 28px; font-weight: 600; line-height: 1; }
  .holder-name .first { color: var(--brand-blue); }
  .holder-name .last { color: var(--brand-red); }
  .holder-role { color: var(--ink-dark); font-size: 14px; font-weight: 500; letter-spacing: 0.6px; margin-top: 4px; }

  .contact { position: absolute; left: 44px; top: 166px; list-style: none; }
  .contact li { display: flex; align-items: center; gap: 10px; font-size: 16px; color: var(--ink-dark); height: 26px; }
  .contact svg { width: 16px; height: 16px; fill: var(--brand-blue); flex: none; }

  .footer-rule { position: absolute; left: 0; right: 0; bottom: 92px; height: 6px; background: var(--brand-red); }
  .footer-band { position: absolute; left: 0; right: 0; bottom: 0; height: 84px; background: var(--brand-blue); }
</style>
</head>
<body>
<main class="sheet">
  <section class="card card-back" aria-label="Card back">
    <div class="brand">
      <span class="brand-dot"></span>
      <div class="brand-text">
        <span class="brand-name">NORTHLINE HAUL</span>
        <span class="brand-tagline">The Auto Transport Professionals</span>
      </div>
    </div>
  </section>

  <section class="card card-front" aria-label="Card front">
    <div class="footer-rule"></div>
    <div class="footer-band"></div>

    <div class="holder">
      <p class="holder-name"><span class="first">DEAN</span> <span class="last">MARSH</span></p>
      <p class="holder-role">DIAPATCHER</p>
    </div>

    <div class="brand">
      <span class="brand-dot"></span>
      <div class="brand-text">
        <span class="brand-name">NORTHLINE HAUL</span>
        <span class="brand-tagline">The Auto Transport Professionals</span>
      </div>
    </div>

    <ul class="contact">
      <li>
        <svg viewBox="0 0 24 24"><path d="M6.6 10.8a15.1 15.1 0 0 0 6.6 6.6l2.2-2.2c.3-.3.7-.4 1-.2 1.1.4 2.3.6 3.6.6.6 0 1 .4 1 1V20c0 .6-.4 1-1 1A17 17 0 0 1 3 4c0-.6.4-1 1-1h3.5c.6 0 1 .4 1 1 0 1.3.2 2.5.6 3.6.1.3 0 .7-.2 1z"/></svg>
        555-014-2287
      </li>
      <li>
        <svg viewBox="0 0 24 24"><path d="M6 2h12v5H6zM4 8h16a2 2 0 0 1 2 2v7h-4v5H6v-5H2v-7a2 2 0 0 1 2-2zm4 8v4h8v-4z"/></svg>
        555-014-2290
      </li>
      <li>
        <svg viewBox="0 0 24 24"><path d="M2 5h20v14H2zm2 2v.5l8 5.5 8-5.5V7zm0 3v7h16v-7l-8 5.5z"/></svg>
        dispatch@northlinehaul.com
      </li>
    </ul>
  </section>
</main>
</body>
</html>
```